Stylish WordPress Web Site for International Young Travellers and Families

We need a WordPress Website with a stylish design for our international online registration and matching solution for Au Pairs and Host Families called Nanny Lantern. We have strong competitors and wish to stand out with a straightforward registration process and fresh design. We need payment facilities and an easy navigation for Au Pairs and Host Families to log in, upload photos, edit their profiles etc. I need it well integrated and automation of payment receipts etc, and connected with PostFinch for newsletters etc. Logos supplied, along with website plan and text for pages. Some text to still be supplied. Can supply stock photos if required. Designer needs to advise. SIte needs to be translated into - French, Spanish, Italian, Dutch, German,

Target Market(s)

Young international travellors (aged 18-28 years) predominately female and Mums aged (28 - 48 years) of 2 or more children.

Industry/Entity Type

E-Commerce

Coding

Coded - Design and coding required

Font styles to use
Sans Serif

Requirements
Must have
• Simple registration. Great photos. Integrated with Post Finch. Payment facilities. Ease of log in for updating profiles, uploading photos etc. Site translated as listed above.
Nice to have
• Would love to see the compass design integrated throughout website.

```html
<!DOCTYPE html>
<html lang="en">
<head>
<meta charset="utf-8">
<title>Nanny Lantern</title>
<link href="https://fonts.googleapis.com/css2?family=Oswald:wght@400;500&family=Noto+Serif:ital,wght@0,400;0,700;1,400&display=swap" rel="stylesheet">
<style>
:root{
  --blue:#29b2e4;
  --slate:#4a4b65;
  --gold:#a69a6a;
  --ink:#333;
  --white:#fff;
  --footer:#27303b;
  --sand:#cdbf94;
}
*{box-sizing:border-box;margin:0;padding:0}
html,body{width:1200px;height:3939px;overflow:hidden}
body{position:relative;background:var(--white);font-family:"Noto Serif",serif;color:var(--ink)}
.abs{position:absolute}
.center{text-align:center}

/* hero */
.hero{left:0;top:0;width:1200px;height:688px;background:linear-gradient(180deg,#3a2d27 0%,#7a5a3e 35%,#b98a55 55%,#5a4230 80%,#2d221c 100%)}
.brand{left:14px;top:14px;width:200px;height:200px}
.brand-dot{position:absolute;left:50px;top:0;width:100px;height:100px;border-radius:50%;background:#2f3a4c;border:3px solid #d8dde3}
.brand-name{position:absolute;left:0;top:114px;width:200px;text-align:center;color:var(--sand);font-size:24px;white-space:nowrap}
.nav{left:372px;top:52px;display:flex;white-space:nowrap}
.nav a{display:block;color:var(--white);text-decoration:none;font-size:17px;height:45px;line-height:45px;padding:0 15px;margin-right:8px;white-space:nowrap}
.nav a.on{background:var(--sand);color:#333;border-radius:23px}
.hero-title{left:0;top:362px;width:1200px;color:var(--white);font-family:Oswald,sans-serif;font-weight:400;font-size:46px;line-height:58px;letter-spacing:.5px;text-shadow:0 2px 6px rgba(0,0,0,.4)}

/* audience boxes */
.panel{top:688px;height:320px;color:var(--white)}
.panel.families{left:10px;width:584px;background:var(--blue);padding:0 44px 0 24px}
.panel.pairs{left:594px;width:580px;background:var(--slate);padding:0 24px 0 44px}
.panel .icon{margin:34px auto 0;width:96px;height:70px;border-radius:8px;background:rgba(255,255,255,.28)}
.panel h2{font-weight:400;font-size:30px;margin-top:16px}
.panel p{font-size:16px;line-height:26px;margin-top:8px;height:78px;overflow:hidden}
.pill{display:inline-block;height:38px;line-height:38px;padding:0 26px;border-radius:19px;font-size:16px;margin-top:12px}
.families .pill{background:var(--slate);color:var(--white)}
.pairs .pill{background:var(--sand);color:var(--white)}
.or{left:557px;top:808px;width:74px;height:74px;border-radius:50%;background:var(--blue);border:3px solid var(--white);color:var(--white);font-size:22px;line-height:68px;text-align:center}

/* welcome */
.welcome-title{left:0;top:1050px;width:1200px;color:var(--blue);font-weight:400;font-size:31px}
.divider{height:20px}
.welcome-text{left:24px;top:1162px;width:1152px;font-size:15.5px;line-height:30px}
.welcome-text p{text-align:center}
.btn-dark{left:525px;top:1356px;width:137px;height:40px;border-radius:20px;background:var(--slate);color:var(--white);font-size:16px;line-height:40px}

/* how it works */
.how{left:0;top:1450px;width:1200px;height:1171px;background:var(--slate)}
.how-title{left:0;top:1490px;width:1200px;color:var(--white);font-weight:400;font-size:31px}
.timeline{left:592px;top:1641px;width:4px;height:736px;background:var(--white)}
.dot{width:74px;height:74px;border-radius:50%;background:var(--blue);border:3px solid var(--white);color:var(--white);font-size:24px;line-height:68px;text-align:center}
.step{background:var(--white);padding:18px 20px;color:#222}
.step h3{color:var(--blue);font-weight:400;font-size:24px}
.step p{font-size:16px;line-height:25px;margin-top:6px}
.art{background:rgba(255,255,255,.85);border-radius:6px}
.tile{width:136px;height:176px;border:3px solid var(--white)}

/* cards */
.card{top:2673px;height:489px;color:var(--white)}
.card .photo{height:229px}
.card h4{font-weight:400;font-size:21px;margin-top:34px;text-align:center}
.card p{font-size:15px;line-height:24px;padding:0 22px;margin-top:12px;text-align:left}
.radios{display:flex;justify-content:center;gap:26px;margin-top:18px;font-size:18px}
.radios span::before{content:"";display:inline-block;width:13px;height:13px;border-radius:50%;background:var(--white);margin-right:8px;vertical-align:-1px}
.select{margin:22px 26px 0;height:40px;border:2px solid var(--white);border-radius:4px;padding:0 14px;font-size:15px;line-height:36px;position:relative}
.select svg{position:absolute;right:12px;top:12px}
.btn-light{display:block;margin:22px auto 0;width:152px;height:42px;border-radius:21px;background:var(--white);font-size:16px;line-height:42px;text-align:center}

/* contact */
.contact{left:0;top:3209px;width:1200px;height:657px;background:linear-gradient(90deg,#1e2126 0%,#3a3531 40%,#2c2d31 100%)}
.contact-title{left:0;top:3238px;width:1200px;color:var(--white);font-weight:400;font-size:31px}
.info{left:13px;color:var(--white);font-size:15px;display:flex;align-items:center;gap:16px;white-space:nowrap}
.social{top:3677px;width:36px;height:36px;border-radius:50%;background:var(--blue)}
.field{background:var(--white);border-radius:27px;color:#555;font-style:italic;font-size:16px;padding-left:24px;line-height:56px;height:56px}
.send{left:1003px;top:3737px;width:171px;height:56px;border-radius:28px;background:var(--blue);color:var(--white);font-style:italic;font-size:19px;line-height:56px}

/* footer */
.footer{left:0;top:3866px;width:1200px;height:73px;background:var(--footer);font-size:14px;color:#c8ced6}
.footer .links{left:13px;top:26px}
.footer .links a{color:var(--blue);text-decoration:none}
.footer .copy{right:20px;top:26px}
.footer .copy b{color:var(--blue);font-weight:400}
</style>
</head>
<body>

<header>
  <div class="abs hero" role="img" aria-label="Photo of a family sitting together outdoors at sunset, seen from behind"></div>
  <div class="abs brand">
    <span class="brand-dot"></span>
    <span class="brand-name">Nanny Lantern</span>
  </div>
  <nav class="abs nav">
    <a class="on">HOME</a><a>ABOUT US</a><a>AU PAIRS</a><a>HOST FAMILIES</a><a>BLOG</a><a>CONTACT US</a>
  </nav>
  <h1 class="abs hero-title center">AN INTERNATIONAL ONLINE REGISTRATION &amp; MATCHING<br>SOLUTION TO FIND YOU THE VERY BEST AU PAIR FOR YOUR FAMILY.</h1>
</header>

<section>
  <div class="abs panel families center">
    <div class="icon" role="img" aria-label="Family icon"></div>
    <h2>HOST FAMILIES</h2>
    <p>Dreaming of sunny days, lounging around the pool with a great book, sipping on an icey cold Mojoto mmm mmmm REALITY! It's not quite the same but isn't it a great dream! Look, chances</p>
    <span class="pill">GET STARTED</span>
  </div>
  <div class="abs panel pairs center">
    <div class="icon" role="img" aria-label="Au pair icon"></div>
    <h2>AU PAIRS</h2>
    <p>Cheap accommodation overseas is just part of what you get when you sign up to Nanny Lantern. You see, we are as dedicated to your adventure as you are. When you have had the</p>
    <span class="pill">GET STARTED</span>
  </div>
  <div class="abs or">OR</div>
</section>

<section>
  <h2 class="abs welcome-title center">WELCOME TO NANNY LANTERN</h2>
  <svg class="abs divider" style="left:440px;top:1101px" width="320" height="20" viewBox="0 0 320 20"><line x1="0" y1="10" x2="148" y2="10" stroke="#29b2e4" stroke-width="2"/><line x1="172" y1="10" x2="320" y2="10" stroke="#29b2e4" stroke-width="2"/><path d="M160 2l3 8-3 8-3-8z M152 10l8-3 8 3-8 3z" fill="#29b2e4"/></svg>
  <div class="abs welcome-text">
    <p>Keeping your world and the little people in it happy, is no easy task. Sometimes that washing pile never gets smaller and wouldn't it be just great knowing that when you get home from work, that dinner is already on the table, the kids feed, bathed and dressed for bed.</p>
    <p>We get it. Life is busy. Probably busier than ever before, with running children around, a job to do, housework, trying to fit in some time to get to the gym and maybe just to be a more balanced, we all need a little help.</p>
    <p>This is where Nanny Lantern can come to the rescue! It's a great solution to childcare, affordable (often cheaper) and gives you so much more. You can find your Nanny Lantern Au Pair, they are a person between the age of 18 and 30 years of age with various skills</p>
  </div>
  <div class="abs btn-dark center">LEARN MORE</div>
</section>

<section>
  <div class="abs how"></div>
  <h2 class="abs how-title center">HOW IT WORKS</h2>
  <svg class="abs divider" style="left:440px;top:1558px" width="320" height="20" viewBox="0 0 320 20"><line x1="0" y1="10" x2="148" y2="10" stroke="#fff" stroke-width="2"/><line x1="172" y1="10" x2="320" y2="10" stroke="#fff" stroke-width="2"/><path d="M160 2l3 8-3 8-3-8z M152 10l8-3 8 3-8 3z" fill="#fff"/></svg>
  <div class="abs timeline"></div>

  <div class="abs step" style="left:84px;top:1610px;width:441px;height:136px">
    <h3>STEP 1</h3>
    <p>All that is required is a straightforward free registrationand enter your search criteria and your ideal candiates profiles will be displayed</p>
  </div>
  <svg class="abs" style="left:525px;top:1628px" width="20" height="36" viewBox="0 0 20 36"><path d="M0 0L20 18L0 36z" fill="#fff"/></svg>
  <div class="abs dot" style="left:557px;top:1609px">1</div>
  <div class="abs art" style="left:664px;top:1607px;width:229px;height:205px" role="img" aria-label="Icon of a computer screen showing a checklist form"></div>

  <div class="abs tile" style="left:84px;top:1864px" role="img" aria-label="Icon of a parent with a child"></div>
  <div class="abs tile" style="left:234px;top:1864px;background:var(--blue)" role="img" aria-label="Icon of a family group"></div>
  <div class="abs tile" style="left:384px;top:1864px" role="img" aria-label="Icon of a woman with a child"></div>
  <div class="abs dot" style="left:557px;top:1869px">2</div>
  <div class="abs step" style="left:664px;top:1864px;width:439px;height:176px">
    <h3>STEP 2</h3>
    <p>Once you have selected your choices you can send a secure message to discuss details further includ interviews and deciding on the perfect Au Pair or Host Family.</p>
  </div>

  <div class="abs step" style="left:84px;top:2096px;width:438px;height:136px">
    <h3>STEP 3</h3>
    <p>Au Pairs book their travel in and Host Families prepare to welcome you into their home.</p>
  </div>
  <div class="abs dot" style="left:557px;top:2095px">3</div>
  <div class="abs art" style="left:683px;top:2075px;width:210px;height:223px" role="img" aria-label="Icon of a traveller pulling a suitcase"></div>

  <div class="abs art" style="left:189px;top:2337px;width:231px;height:210px" role="img" aria-label="Icon of a computer screen showing profile windows"></div>
  <div class="abs dot" style="left:557px;top:2340px">4</div>
  <div class="abs step" style="left:664px;top:2345px;width:439px;height:158px">
    <h3>STEP 4</h3>
    <p>Once your have made your choice you can choose to make you profile inactive and easily reinstate it again when you are being searching again</p>
  </div>
</section>

<section>
  <div class="abs card" style="left:10px;width:376px;background:var(--blue)">
    <div class="photo" role="img" aria-label="Photo of a parent and child sitting on a jetty by the sea" style="background:linear-gradient(180deg,#8fa3a8,#5c6a6a 60%,#3e4a4c)"></div>
    <h4>REGISTER FREE AS:</h4>
    <div class="radios"><span>Au Pair</span><span>Host Familes</span></div>
    <div class="select">Select Country<svg width="14" height="10" viewBox="0 0 14 10"><path d="M0 0h14L7 10z" fill="#fff"/></svg></div>
    <div class="btn-light" style="color:var(--blue)">SING UP NOW</div>
  </div>
  <div class="abs card" style="left:407px;width:370px;background:var(--slate)">
    <div class="photo" role="img" aria-label="Photo of a family walking together through a sunny field" style="background:linear-gradient(180deg,#e9d7a6,#c9a56a 55%,#8f7a45)"></div>
    <h4 style="margin-top:28px">WHY NANNY LANTERN ?</h4>
    <p>We believe in the product – that's right you! Wendell Marsh said it well, "Do what you do so well that they will want to see it again and bring their friends." Creating love</p>
    <div class="btn-light" style="color:var(--slate);margin-top:12px">LEARN MORE</div>
  </div>
  <div class="abs card" style="left:806px;width:368px;background:var(--gold)">
    <div class="photo" role="img" aria-label="Photo of parents and a child lying together on the grass" style="background:linear-gradient(180deg,#9cc46a,#6f9a3d 55%,#4e7128)"></div>
    <h4>MEMBERSHIP</h4>
    <div class="radios"><span>Au Pair</span><span>Host Familes</span></div>
    <div class="select">Basic<svg width="14" height="10" viewBox="0 0 14 10"><path d="M0 0h14L7 10z" fill="#fff"/></svg></div>
    <div class="btn-light" style="color:var(--gold)">SING UP NOW</div>
  </div>
</section>

<section>
  <div class="abs contact" role="img" aria-label="Dimmed photo of a mother and child as background"></div>
  <h2 class="abs contact-title center">HOW TO CONTACT US</h2>
  <svg class="abs divider" style="left:440px;top:3304px" width="320" height="20" viewBox="0 0 320 20"><line x1="0" y1="10" x2="148" y2="10" stroke="#fff" stroke-width="2"/><line x1="172" y1="10" x2="320" y2="10" stroke="#fff" stroke-width="2"/><path d="M160 2l3 8-3 8-3-8z M152 10l8-3 8 3-8 3z" fill="#fff"/></svg>

  <div class="abs info" style="top:3385px">
    <svg width="26" height="24" viewBox="0 0 26 24"><path d="M13 1L1 12h4v11h6v-7h4v7h6V12h4z" fill="#29b2e4"/></svg>
    <div>NANNY LANTERN<br>Coral Bay Shore, Eastland AUSTRALIA</div>
  </div>
  <div class="abs info" style="top:3465px">
    <svg width="26" height="26" viewBox="0 0 26 26"><path d="M6 2l5 5-3 3c1 3 4 6 7 8l3-3 5 5-3 4C11 24 2 15 2 6z" fill="#29b2e4"/></svg>
    <div>61 400 218 604</div>
  </div>
  <div class="abs info" style="top:3535px">
    <svg width="26" height="20" viewBox="0 0 26 20"><rect width="26" height="20" rx="2" fill="#29b2e4"/><path d="M1 2l12 9 12-9" stroke="#fff" stroke-width="2" fill="none"/></svg>
    <div>info@nannylantern.com</div>
  </div>
  <div class="abs info" style="top:3598px">
    <svg width="26" height="26" viewBox="0 0 26 26"><circle cx="13" cy="13" r="12" fill="#29b2e4"/><path d="M13 6v7h5" stroke="#fff" stroke-width="2" fill="none"/></svg>
    <div>Monday – Friday 8am – 6pm AEST</div>
  </div>
  <div class="abs social" style="left:11px"></div>
  <div class="abs social" style="left:58px"></div>
  <div class="abs social" style="left:105px"></div>
  <div class="abs social" style="left:155px"></div>
  <div class="abs social" style="left:205px"></div>
  <div class="abs social" style="left:252px"></div>

  <div class="abs field" style="left:412px;top:3386px;width:365px">First Name *</div>
  <div class="abs field" style="left:806px;top:3386px;width:368px">Last Name*</div>
  <div class="abs field" style="left:412px;top:3466px;width:365px">Email Address *</div>
  <div class="abs field" style="left:806px;top:3466px;width:368px">Subject*</div>
  <div class="abs field" style="left:412px;top:3545px;width:762px;height:171px;border-radius:20px;line-height:22px;padding-top:20px">Message *</div>
  <div class="abs send center">Send Message</div>
</section>

<footer class="abs footer">
  <div class="abs links"><a>Home</a> &nbsp;/&nbsp; <a>About us</a> &nbsp;/&nbsp; <a>Au Pair</a> &nbsp;/&nbsp; <a>Host Families</a> &nbsp;/&nbsp; <a>Blog</a> &nbsp;/&nbsp; <a>Contacts Us</a></div>
  <div class="abs copy">Copyright © 2016 <b>Nanny Lantern</b> All rights reserved.</div>
</footer>

</body>
</html>
```